Getränkefachhandel sucht Etiketten-Design für zwei Edelbrände
Zielgruppe
Wir sind ein Getränkefachhandel mit eigenen Getränkemärkten, dazu stellen wir Edelbrände her. Die Vermarktung läuft über unsere Getränkemärkte und die Gastronomie. Unsere bisherige Spirituosenlinie ist klassisch geprägt. In den letzten Monaten haben wir einen Gin mit abweichender Flasche und Design auf den Markt gebracht. Dies hat unsere Käuferschicht verjüngt. Deshalb wollen wir 2 klassische Edelbrände (Williams und Kirsch) in einer veränderten Qualität auf den markt bringen. Bilder sind beigefügt.
Aufgabenstellung
Keine besonderen Vorgaben. Das Design soll der neuen Gin-Linie angepasst werden und von der bisherigen Linie abweichen. Als Flasche wird nicht die klassische Longneckflasche, sondern die bauchige Ginflasche eingesetzt. Beide Flaschen haben 0,5 ltr. Inhalt. Es muss ein Feld für eine Losnummer, die bei der Abfüllung eingedruckt wird, vorbereitet werden. Die Produkte sind klassische Edelbrände mit Fruchtauszügen verfeinert, haben also eine goldgelbe (Williams) und rote (Kirsch) Farbe. Die Bezeichnungen lauten : Premium Williams Birne als Headliner und dem Zusatz Feine Spirituose mit Fruchtauszügen verfeinert, bzw. Premium Kirsche als Headliner und dem Zusatz Feine Spirituose mit Fruchtauszügen verfeinert. Evtl. können Fruchtbilder eingefügt werden. Vorgeschriebene Pflichtangaben sind : Inhalt 0,5 L und 37 % vol., sowie unsere Firmierung und Anschrift : Getränke Wolsink GmbH & Co. Brennerei und Mosterei KG, Lindauer Str. 31 - 33, 70327 Stuttgart. Diese Angaben können evtl. auch auf einem kleinen Zusatzetikett wie beim Gin angebracht werden. Ebenso die Losnummer. Die Deckelfarbe kann entweder in Holzoptik oder auch in Farbe gewählt werden.

```html
<!DOCTYPE html>
<html lang="de">
<head>
<meta charset="utf-8">
<title>Premium Edelbrände – Etiketten</title>
<link rel="stylesheet" href="https://fonts.googleapis.com/css2?family=Amatic+SC:wght@400;700&family=Allura&family=Roboto+Condensed:wght@400;700&display=swap">
<style>
  :root {
    --bg: #f1f1f2;
    --panel: #ffffff;
    --cherry-label: #b06466;
    --cherry-mark: #d98f9c;
    --cherry-fruit: #9c1c2a;
    --cherry-soft: #e9b8c0;
    --pear-label: #fde7b6;
    --pear-mark: #e2c400;
    --pear-fruit: #c9b431;
    --pear-soft: #f5dd16;
    --ink-dark: #3b2226;
    --ink-grey: #4b505c;
    --pear-claim: #ffffff;
    --white: #ffffff;
    --pear-back: #f8d80c;
    --cherry-back: #b35f6b;
    --pear-back-ink: #2a2410;
  }
  * { box-sizing: border-box; margin: 0; padding: 0; }
  html, body { width: 1200px; height: 517px; overflow: hidden; background: var(--bg); }
  .canvas {
    width: 1200px; height: 517px;
    display: grid; grid-template-columns: repeat(4, 1fr);
    gap: 12px; padding: 18px 14px;
  }
  .panel {
    background: var(--panel);
    display: flex; flex-direction: column; align-items: center;
    padding-top: 40px;
  }
  .neck-mark {
    display: flex; align-items: center; gap: 6px;
    height: 24px; margin-bottom: 48px;
    font-family: "Roboto Condensed", sans-serif; font-size: 13px; font-weight: 700;
  }
  .neck-mark .dot { width: 9px; height: 9px; }
  .neck-mark.cherry { color: var(--cherry-mark); }
  .neck-mark.cherry .dot { background: var(--cherry-mark); }
  .neck-mark.pear { color: var(--pear-mark); }
  .neck-mark.pear .dot { background: var(--pear-mark); }
  .front-label {
    width: 230px; height: 360px;
    display: flex; flex-direction: column; align-items: center;
    padding-top: 20px;
  }
  .front-label.cherry { background: var(--cherry-label); }
  .front-label.pear { background: var(--pear-label); }
  .premium {
    font-family: "Amatic SC", sans-serif; font-size: 30px; letter-spacing: 7px;
    line-height: 1;
  }
  .cherry .premium { color: var(--ink-dark); }
  .pear .premium { color: var(--ink-grey); }
  .variety {
    font-family: "Amatic SC", sans-serif; font-size: 46px; line-height: 1.05;
    margin-top: 2px; white-space: nowrap;
  }
  .cherry .variety { color: var(--white); }
  .pear .variety { color: var(--ink-grey); font-size: 40px; }
  .fruit {
    width: 190px; height: 135px; margin-top: 16px; border-radius: 50%;
  }
  .cherry .fruit { background: radial-gradient(circle at 50% 55%, var(--cherry-fruit) 0 30%, var(--cherry-soft) 60%, transparent 72%); }
  .pear .fruit { background: radial-gradient(circle at 50% 55%, var(--pear-fruit) 0 30%, var(--pear-soft) 60%, transparent 72%); }
  .claim {
    font-family: "Allura", cursive; font-size: 21px; line-height: 1.1;
    text-align: center; margin-top: 18px; color: var(--pear-claim);
  }
  .cherry .claim { color: var(--white); }
  .back-label {
    margin-top: 50px; width: 200px; border-radius: 12px; padding: 6px;
  }
  .back-label.cherry { background: var(--cherry-back); }
  .back-label.pear { background: var(--pear-back); }
  .back-label .frame {
    border: 2px solid var(--white); border-radius: 9px;
    font-family: "Roboto Condensed", sans-serif; font-size: 11px;
  }
  .back-label.cherry .frame { color: var(--white); }
  .back-label.pear .frame { color: var(--pear-back-ink); }
  .row { border-bottom: 1.5px solid var(--white); padding: 5px 8px; font-weight: 700; }
  .row.split { display: grid; grid-template-columns: 1fr 2fr; padding: 0; }
  .row.split span { padding: 5px 8px; }
  .row.split span + span { border-left: 1.5px solid var(--white); }
  .row.address { padding: 7px 8px 6px; line-height: 1.25; border-bottom: none; font-weight: 400; }
  .lot {
    margin: 4px 8px 9px; background: var(--white); color: #222;
    text-align: center; letter-spacing: 3px; font-size: 11px; padding: 3px 0;
  }
</style>
</head>
<body>
<main class="canvas">
  <section class="panel">
    <div class="neck-mark cherry"><span class="dot"></span><span>Wolsink Getränkemarkt</span></div>
    <div class="front-label cherry">
      <div class="premium">Premium</div>
      <div class="variety">Kirsche</div>
      <div class="fruit" role="img" aria-label="Foto von Kirschen mit Blatt auf rosa Pinselstrich"></div>
      <p class="claim">Feine Spirituose<br>mit Fruchtauszügen<br>verfeinert</p>
    </div>
  </section>

  <section class="panel">
    <div class="neck-mark cherry"><span class="dot"></span><span>Wolsink Getränkemarkt</span></div>
    <div class="back-label cherry">
      <div class="frame">
        <div class="row">BATCH №</div>
        <div class="row">BOTLE №</div>
        <div class="row split"><span>50cl</span><span>37% vol.</span></div>
        <div class="row address">Getränke Wolsink GmbH &amp; Co. Brennerei und Mosterei KG, Lindauer Str. 31 - 33, 70327 Stuttgart</div>
        <div class="lot">L0404</div>
      </div>
    </div>
  </section>

  <section class="panel">
    <div class="neck-mark pear"><span class="dot"></span><span>Wolsink Getränkemarkt</span></div>
    <div class="front-label pear">
      <div class="premium">Premium</div>
      <div class="variety">Williams Birne</div>
      <div class="fruit" role="img" aria-label="Foto von zwei Williams-Birnen auf gelbem Pinselstrich"></div>
      <p class="claim">Feine Spirituose<br>mit Fruchtauszügen<br>verfeinert</p>
    </div>
  </section>

  <section class="panel">
    <div class="neck-mark pear"><span class="dot"></span><span>Wolsink Getränkemarkt</span></div>
    <div class="back-label pear">
      <div class="frame">
        <div class="row">BATCH №</div>
        <div class="row">BOTLE №</div>
        <div class="row split"><span>50cl</span><span>37% vol.</span></div>
        <div class="row address">Getränke Wolsink GmbH &amp; Co. Brennerei und Mosterei KG, Lindauer Str. 31 - 33, 70327 Stuttgart</div>
        <div class="lot">L0404</div>
      </div>
    </div>
  </section>
</main>
</body>
</html>
```